Website design for labour force (commercial truck driver) company

Looking for a Wordpress template (or design files in conjunction with a free Wordpress template).
Company tag line:
CargoLoop – On Demand, Professional Drivers
Real Drivers | Real Standards | Real Results
Logo design has already been completed and is attached

Company provides contract drivers to trucking companies. Target market is both the trucking companies looking for drivers and drivers looking for work.
Design to encompass header / footer and basic page design, navigation menu, home page, contact page. Customer will add content and additional pages over time.

```html
<!DOCTYPE html>
<html lang="en">
<head>
<meta charset="utf-8">
<title>CargoLoop – On Demand, Professional Drivers</title>
<link rel="stylesheet" href="https://fonts.googleapis.com/css2?family=Poppins:wght@400;500;600;700;800&display=swap">
<style>
:root{
  --green:#15895f;
  --ink:#1f1f1f;
  --muted:#4a4a4a;
  --grey:#e6e5e5;
  --photo-light:#d9d7d5;
  --photo-dark:#b3afab;
  --white:#ffffff;
  --black:#0d0d0d;
}
*{box-sizing:border-box;margin:0;padding:0}
html,body{width:1200px;height:3670px;overflow:hidden}
body{font-family:'Poppins',sans-serif;color:var(--ink);background:var(--white);position:relative}
section,header,footer{position:absolute;left:0;width:1200px}
.pill{position:absolute;display:flex;align-items:center;justify-content:center;border-radius:40px;font-weight:600;font-size:15px;text-decoration:none}
.pill-green{background:var(--green);color:var(--white)}
.pill-white{background:var(--white);color:var(--ink)}
.pill-outline{border:2px solid var(--white);color:var(--white)}
.brand{font-weight:700;display:flex;align-items:center;gap:10px;white-space:nowrap}
.brand-dot{border-radius:50%;background:var(--green);flex-shrink:0}

/* header */
.site-header{top:0;height:67px;background:var(--white)}
.site-header .brand{position:absolute;left:75px;top:15px;font-size:24px;color:var(--ink)}
.site-header .brand-dot{width:26px;height:26px;background:var(--ink)}
.nav{position:absolute;top:22px;left:524px;display:flex;gap:52px;font-size:15px;font-weight:500}
.nav a{color:var(--ink);text-decoration:none;display:flex;align-items:center;gap:10px}
.nav-contact{left:990px;top:15px;width:135px;height:37px}

/* hero */
.hero{top:67px;height:616px}
.hero-photo{position:absolute;inset:0;background:linear-gradient(90deg,#6d7570 0%,#8a8f88 35%,#8c6a5c 62%,#3e5670 100%)}
.hero-shade{position:absolute;inset:0;background:linear-gradient(90deg,rgba(0,0,0,.35),rgba(0,0,0,0) 60%)}
.hero h1{position:absolute;left:73px;top:160px;color:var(--white);font-size:62px;font-weight:800;line-height:67px}
.hero .tagline{position:absolute;left:73px;top:366px;color:var(--white);font-size:25px}
.hero .b1{left:75px;top:423px;width:135px;height:37px}
.hero .b2{left:224px;top:423px;width:168px;height:37px}

/* about */
.about{top:683px;height:577px}
.about-photo{position:absolute;left:0;top:95px;width:620px;height:482px;background:linear-gradient(135deg,var(--photo-light),var(--photo-dark))}
.about .eyebrow{position:absolute;left:656px;top:86px;color:var(--green);font-weight:700;font-size:22px}
.about h2{position:absolute;left:656px;top:117px;font-size:30px;font-weight:700;line-height:34px;width:480px}
.about p{position:absolute;left:658px;top:197px;width:420px;font-size:11.5px;line-height:16.5px}
.about .read{left:658px;top:303px;width:135px;height:37px}

/* why */
.why{top:1260px;height:437px}
.why h2{position:absolute;top:82px;width:100%;text-align:center;font-size:30px;font-weight:700}
.features{position:absolute;left:74px;top:172px;width:1045px;height:197px;display:flex}
.feature{flex:1;border-left:1px solid #d6d6d6;padding:22px 22px 0 22px;position:relative}
.feature:first-child{border-left:none}
.feature svg{width:62px;height:62px}
.feature h3{position:absolute;bottom:60px;left:22px;font-size:18px;font-weight:600;line-height:23px}
.feature p{position:absolute;top:142px;left:22px;font-size:12px;line-height:16.5px;color:var(--muted);width:215px}

/* how */
.how{top:1697px;height:441px;background:var(--green)}
.how h2{position:absolute;top:50px;width:100%;text-align:center;color:var(--white);font-size:30px;font-weight:700}
.step{position:absolute;top:106px;width:260px;height:273px;border-radius:4px;overflow:hidden}
.step-photo{position:absolute;inset:0}
.step-shade{position:absolute;inset:0;background:linear-gradient(180deg,rgba(0,0,0,0) 50%,rgba(0,0,0,.65))}
.step h3{position:absolute;left:14px;bottom:40px;color:var(--white);font-size:18px;font-weight:600}
.step p{position:absolute;left:14px;bottom:22px;color:var(--white);font-size:12px}

/* driver */
.driver{top:2138px;height:330px}
.driver h2{position:absolute;left:204px;top:132px;font-size:30px;font-weight:700}
.driver p{position:absolute;left:204px;top:178px;width:420px;font-size:11.5px;line-height:16.5px}
.driver .apply{left:204px;top:238px;width:135px;height:37px}
.driver .brand{position:absolute;left:690px;top:118px;font-size:72px;color:var(--ink)}
.driver .brand-dot{width:56px;height:56px}

/* testimonials */
.testimonials{top:2468px;height:520px}
.quote-mark{position:absolute;left:92px;top:-32px;font-size:240px;font-weight:800;color:var(--grey);line-height:1}
.testimonials h2{position:absolute;top:32px;width:100%;text-align:center;font-size:30px;font-weight:700}
.card{position:absolute;top:173px;width:273px;height:263px;background:var(--white);box-shadow:0 6px 22px rgba(0,0,0,.08)}
.card-photo{position:absolute;top:-67px;left:37px;width:198px;height:168px;border-radius:2px;display:flex;align-items:center;justify-content:center}
.play{width:26px;height:26px;border:2px solid var(--white);border-radius:50%;display:flex;align-items:center;justify-content:center}
.stars{position:absolute;top:113px;width:100%;text-align:center;color:var(--green);font-size:16px;letter-spacing:2px}
.card p{position:absolute;top:141px;left:24px;right:24px;text-align:center;font-size:11.5px;line-height:17px;color:var(--muted)}
.person{position:absolute;top:215px;width:100%;display:flex;justify-content:center;align-items:center;gap:6px}
.avatar{width:24px;height:24px;border-radius:50%;background:#7a8c9e}
.person b{display:block;font-size:12.5px;font-weight:600;line-height:13px}
.person span{display:block;font-size:9px;color:#999}

/* cta + footer */
.cta{top:2988px;height:682px;background:linear-gradient(180deg,var(--white) 0,var(--white) 130px,var(--black) 130px)}
.cta-band{position:absolute;left:74px;top:7px;width:1052px;height:268px;border-radius:134px;background:var(--green);overflow:hidden}
.cta-left{position:absolute;left:0;top:0;width:440px;height:268px;background:var(--white);border-radius:134px 0 0 134px}
.cta-left .brand{position:absolute;left:80px;top:104px;font-size:52px;color:var(--green)}
.cta-left .brand-dot{width:40px;height:40px}
.cta h2{position:absolute;left:674px;top:85px;color:var(--white);font-size:30px;font-weight:700;line-height:34px}
.cta .sub{position:absolute;left:675px;top:153px;color:var(--white);font-size:12px}
.cta .c1{left:674px;top:183px;width:150px;height:37px}
.cta .c2{left:834px;top:183px;width:136px;height:37px}
.vline{position:absolute;top:311px;width:1px;height:171px;background:#6a6a6a}
.footer-brand{position:absolute;left:0;top:354px;width:100%;justify-content:center;font-size:62px;color:var(--white)}
.footer-brand .brand-dot{width:50px;height:50px;background:var(--white)}
.hr{position:absolute;left:140px;width:929px;height:1px;background:#5a5a5a}
.contact{position:absolute;top:538px;display:flex;gap:16px;color:var(--white)}
.contact .ico{width:50px;height:50px;border-radius:50%;background:var(--green);display:flex;align-items:center;justify-content:center;flex-shrink:0}
.contact b{display:block;color:var(--green);font-size:15px;font-weight:600;line-height:18px;margin-top:6px}
.contact span{display:block;font-size:12px;line-height:15px}
.social{position:absolute;left:834px;top:541px;display:flex;gap:6px}
.social i{width:43px;height:43px;border-radius:50%;background:#2a2a2a;display:block}
.social i.on{background:var(--green)}
.copyright{position:absolute;top:647px;width:100%;text-align:center;color:var(--white);font-size:12px}
</style>
</head>
<body>

<header class="site-header">
  <div class="brand"><span class="brand-dot"></span>CargoLoop</div>
  <nav class="nav">
    <a href="#"><svg width="14" height="12" viewBox="0 0 14 12"><path d="M7 0L0 6h2v6h4V8h2v4h4V6h2z" fill="#15895f"/></svg>Hire a Driver</a>
    <a href="#">Find Driving Jobs</a>
    <a href="#">About Us</a>
  </nav>
  <a class="pill pill-green nav-contact">Contact us</a>
</header>

<section class="hero">
  <div class="hero-photo" role="img" aria-label="Truck driver in a plaid shirt sitting in the open door of a truck cab"></div>
  <div class="hero-shade"></div>
  <h1>Professional<br>Drivers When<br>You Need Them</h1>
  <div class="tagline">Reliable. Experienced. Ready to Roll.</div>
  <a class="pill pill-white b1">Hire a Driver</a>
  <a class="pill pill-outline b2">Find Driving Jobs</a>
</section>

<section class="about">
  <div class="about-photo" role="img" aria-label="Photo of a row of parked semi-truck cabs"></div>
  <div class="eyebrow">About Us</div>
  <h2>CargoLoop – On Demand, Professional Drivers</h2>
  <p>At CargoLoop, we connect trucking companies with qualified, contract drivers — fast. Whether you're looking to fill a last-minute shift or build a long-term partnership, our experienced drivers are ready to hit the road. We believe in high standards, safety, and results that move your business forward.</p>
  <a class="pill pill-green read">Read More</a>
</section>

<section class="why">
  <h2>Why Choose CargoLoop?</h2>
  <div class="features">
    <div class="feature">
      <svg viewBox="0 0 62 62" fill="none" stroke="#15895f" stroke-width="2"><circle cx="31" cy="16" r="10"/><path d="M12 58V46c0-8 8-13 19-13s19 5 19 13v12"/><circle cx="31" cy="48" r="7"/></svg>
      <h3>Vetted,<br>Professional Drivers</h3>
      <p>All drivers are background -checked, licensed, &amp; experienced.</p>
    </div>
    <div class="feature">
      <svg viewBox="0 0 62 62" fill="none" stroke="#15895f" stroke-width="2"><circle cx="31" cy="31" r="20"/><circle cx="31" cy="31" r="12"/><circle cx="31" cy="31" r="5"/><path d="M6 10h12M44 52h12M6 10v8M56 52v-8"/></svg>
      <h3>Flexible Contracts</h3>
      <p>On-demand or long-term — we adapt to your needs.</p>
    </div>
    <div class="feature">
      <svg viewBox="0 0 62 62" fill="none" stroke="#15895f" stroke-width="2"><circle cx="28" cy="28" r="24"/><path d="M4 28h48M28 4c-8 8-8 40 0 48M28 4c8 8 8 40 0 48"/><rect x="34" y="38" width="24" height="14" fill="#fff"/><circle cx="40" cy="54" r="3"/><circle cx="52" cy="54" r="3"/></svg>
      <h3>Nationwide Network</h3>
      <p>Wherever you are, we've got drivers near you.</p>
    </div>
    <div class="feature">
      <svg viewBox="0 0 62 62" fill="none" stroke="#15895f" stroke-width="2"><circle cx="31" cy="22" r="11"/><path d="M16 22a15 15 0 0 1 30 0M14 20v8h4v-8zM44 20v8h4v-8zM46 28c0 4-5 6-12 6"/><path d="M12 58v-8c0-7 8-11 19-11s19 4 19 11v8"/></svg>
      <h3>Driver Support</h3>
      <p>We support our drivers with 24/7 help, training, and guidance.</p>
    </div>
  </div>
</section>

<section class="how">
  <h2>How It Works</h2>
  <div class="step" style="left:192px">
    <div class="step-photo" role="img" aria-label="Businessman and colleague in a car reviewing paperwork" style="background:linear-gradient(160deg,#c9c3bc,#5c5955)"></div>
    <div class="step-shade"></div>
    <h3>Request a Driver</h3><p>Submit your job details</p>
  </div>
  <div class="step" style="left:467px">
    <div class="step-photo" role="img" aria-label="Excited man holding a phone and celebrating" style="background:linear-gradient(160deg,#d8d2c6,#4f5a3a)"></div>
    <div class="step-shade"></div>
    <h3>Get Matched Fast</h3><p>We assign a qualified driver</p>
  </div>
  <div class="step" style="left:748px">
    <div class="step-photo" role="img" aria-label="Happy woman leaning out of a car window on the road" style="background:linear-gradient(160deg,#b9c9d6,#7c8a8e)"></div>
    <div class="step-shade"></div>
    <h3>Drive with Confidence</h3><p>Reliable, professional service</p>
  </div>
</section>

<section class="driver">
  <h2>Are You a Driver?</h2>
  <p>Join the CargoLoop network and start getting real driving jobs. We connect professional CDL drivers with top-paying opportunities.</p>
  <a class="pill pill-green apply">Apply Now</a>
  <div class="brand"><span class="brand-dot"></span>CargoLoop</div>
</section>

<section class="testimonials">
  <div class="quote-mark">“</div>
  <h2>Testimonials</h2>
  <div class="card" style="left:174px">
    <div class="card-photo" role="img" aria-label="Two people talking in a car" style="background:linear-gradient(150deg,#a9b3b8,#4d5a60)"><span class="play"><svg width="8" height="10" viewBox="0 0 8 10"><path d="M0 0l8 5-8 5z" fill="#fff"/></svg></span></div>
    <div class="stars">★★★★★</div>
    <p>CargoLoop helped us stay on sched-ule during a busy season. The driver showed up on time, was well-trained, and professional."</p>
    <div class="person"><span class="avatar"></span><div><b>Mara Quill</b><span>Student</span></div></div>
  </div>
  <div class="card" style="left:470px">
    <div class="card-photo" role="img" aria-label="Smiling driver in a truck cab" style="background:linear-gradient(150deg,#b7bcc0,#5a6670)"><span class="play"><svg width="8" height="10" viewBox="0 0 8 10"><path d="M0 0l8 5-8 5z" fill="#fff"/></svg></span></div>
    <div class="stars">★★★★★</div>
    <p>CargoLoop helped us stay on sched-ule during a busy season. The driver showed up on time, was well-trained, and professional."</p>
    <div class="person"><span class="avatar" style="background:#b08a80"></span><div><b>Tessa Brandt</b><span>Student</span></div></div>
  </div>
  <div class="card" style="left:760px">
    <div class="card-photo" role="img" aria-label="Driver at the wheel inside a car" style="background:linear-gradient(150deg,#9aa2a8,#3e464c)"><span class="play"><svg width="8" height="10" viewBox="0 0 8 10"><path d="M0 0l8 5-8 5z" fill="#fff"/></svg></span></div>
    <div class="stars">★★★★★</div>
    <p>CargoLoop helped us stay on sched-ule during a busy season. The driver showed up on time, was well-trained, and professional."</p>
    <div class="person"><span class="avatar" style="background:#34465e"></span><div><b>Leo Farrow</b><span>Student</span></div></div>
  </div>
</section>

<footer class="cta">
  <div class="cta-band">
    <div class="cta-left"><div class="brand"><span class="brand-dot"></span>CargoLoop</div></div>
  </div>
  <h2>Ready to drive your<br>business forward?</h2>
  <div class="sub">Let CargoLoop provide the talent you need.</div>
  <a class="pill pill-white c1">Apply to Drive</a>
  <a class="pill pill-outline c2">Hire a Driver</a>

  <div class="vline" style="left:268px"></div>
  <div class="vline" style="left:942px"></div>
  <div class="brand footer-brand"><span class="brand-dot"></span>CargoLoop</div>

  <div class="hr" style="top:502px"></div>
  <div class="contact" style="left:140px">
    <span class="ico"><svg width="20" height="15" viewBox="0 0 20 15"><rect width="20" height="15" rx="2" fill="#fff"/><path d="M1 1l9 7 9-7" stroke="#15895f" stroke-width="2" fill="none"/></svg></span>
    <div><b>Email</b><span>info@cargoloop.com</span></div>
  </div>
  <div class="contact" style="left:370px">
    <span class="ico"><svg width="14" height="20" viewBox="0 0 14 20"><path d="M7 0a7 7 0 0 0-7 7c0 5 7 13 7 13s7-8 7-13a7 7 0 0 0-7-7z" fill="#fff"/><circle cx="7" cy="7" r="2.5" fill="#15895f"/></svg></span>
    <div><b>location</b><span>88 Haulage Road, Fairview,<br>TX 75000</span></div>
  </div>
  <div class="contact" style="left:606px">
    <span class="ico"><svg width="18" height="18" viewBox="0 0 18 18"><path d="M3 0l4 4-2 3c1 2 4 5 6 6l3-2 4 4-3 3C8 18 0 10 0 3z" fill="#fff"/></svg></span>
    <div><b>Phone</b><span>(800) 555-0142</span></div>
  </div>
  <div class="social"><i></i><i></i><i class="on"></i><i></i><i></i></div>
  <div class="hr" style="top:627px"></div>
  <div class="copyright">Copyright 2025 © CargoLoop Limited LLC All Rights Reserved.</div>
</footer>

</body>
</html>
```